Dorn Studio 817 the new wave for sound to enlighten open ears

This is a music recording studio, we need pictures of a booth, random pictures of anything that will draw interest to a recording studio, we just need the website to reflect a music studio recording website. Apply generic information on the site that correlates with most music studio websites up to date. We want the modern style look that will entice eyes across the nation. Information should be easily accessible on the website. Dorn Studio 817 is owned by Leonard Vasquez located 6172 Bramwell Ct, Miramar, Fl, 33081. Email: Lvasquezstudio@quillmarkpost.com and best contact number to date is 417-392-7048. The sound coming out of this location will be radio ready at all times, artist come in one way and come out with more wisdom than before. Its the new way to make music the appropriate way and bring the best out of those willing to reach their peak.

Target Market(s)

Recording Artist

Industry/Entity Type

Recording Studio

Coding

Coded - Design and coding required

Number of Pages Required

1 page

Font styles to use
Sans Serif

Requirements
Must have
• Anything that gives the site a music feel
Nice to have
• microphones, booths, studio mixing desk

```html
<!DOCTYPE html>
<html lang="en">
<head>
<meta charset="utf-8">
<title>Dorn Studio 817 — Music Recording Studio</title>
<link rel="stylesheet" href="https://fonts.googleapis.com/css2?family=Montserrat:wght@300;400;500;600;700&display=swap">
<style>
:root{
  --ink:#111111;
  --text:#333333;
  --muted:#777777;
  --line:#d4d4d4;
  --white:#ffffff;
  --grey-band:#ececec;
  --black-band:#000000;
  --price-line:#3a3a3a;
  --soc-1:#3b5ea8;
  --soc-2:#2aa3e0;
  --soc-3:#e0452e;
}
*{box-sizing:border-box;margin:0;padding:0}
html,body{width:1200px;height:4337px;overflow:hidden;background:var(--white)}
body{font-family:"Montserrat",Arial,sans-serif;color:var(--text)}
.page{position:relative;width:1200px;height:4337px;overflow:hidden}
.abs{position:absolute}

/* top bar */
.topbar{position:absolute;top:0;left:0;width:1200px;height:40px;border-bottom:1px solid #eee;font-size:11px;color:var(--text)}
.topbar .follow{left:133px;top:12px;display:flex;align-items:center;gap:10px}
.topbar .dot{width:9px;height:9px;border-radius:50%;background:var(--ink)}
.topbar .contact{right:133px;top:9px;display:flex;align-items:center;gap:8px}
.sq-icon{width:20px;height:20px;background:var(--ink);display:flex;align-items:center;justify-content:center}

/* nav */
.nav{position:absolute;top:40px;left:0;width:1200px;height:82px}
.brand{position:absolute;left:133px;top:22px;display:flex;align-items:center;gap:10px;font-size:22px;font-weight:400;color:var(--ink);white-space:nowrap}
.brand .mark{width:34px;height:34px;background:var(--ink)}
.menu{position:absolute;left:440px;top:26px;display:flex;list-style:none;font-size:12px;font-weight:500;color:var(--ink)}
.menu li{padding:8px 14px;margin-right:11px}
.menu li.active{background:var(--ink);color:var(--white)}

/* hero: studio control room photo area */
.hero{position:absolute;top:122px;left:0;width:1200px;height:601px;
  background:
    radial-gradient(ellipse 520px 230px at 50% 62%,rgba(240,170,90,.75),rgba(240,170,90,0) 70%),
    radial-gradient(ellipse 260px 200px at 17% 40%,rgba(150,80,40,.6),rgba(150,80,40,0) 70%),
    radial-gradient(ellipse 260px 200px at 83% 40%,rgba(150,80,40,.6),rgba(150,80,40,0) 70%),
    linear-gradient(180deg,#2a1a12 0%,#5a3220 30%,#8a4e26 55%,#c27a3c 72%,#3a2216 100%)}
.hero h1{position:absolute;top:432px;width:100%;text-align:center;color:var(--white);font-size:34px;font-weight:700;letter-spacing:1px;text-shadow:0 2px 8px rgba(0,0,0,.5)}
.hero .btn{position:absolute;left:518px;top:506px;width:167px;height:43px;border:1px solid var(--white);color:var(--white);font-size:16px;display:flex;align-items:center;justify-content:center;letter-spacing:1px}
.slide-arrow{position:absolute;top:272px;width:46px;height:46px;background:rgba(0,0,0,.75);display:flex;align-items:center;justify-content:center}

/* headings */
.heading{position:absolute;width:100%;text-align:center;font-size:30px;font-weight:400;letter-spacing:2px;color:var(--ink)}
.rule{position:absolute;left:556px;width:88px;height:2px;background:var(--ink)}

/* services */
.services{position:absolute;top:723px;left:0;width:1200px;height:726px}
.card{position:absolute;top:205px;width:299px;height:420px;border:1px solid var(--line);background:var(--white)}
.card .photo{height:342px}
.card p{text-align:center;font-size:14px;letter-spacing:1px;margin-top:30px;color:var(--ink)}
.photo-faders{background:
  radial-gradient(ellipse 160px 120px at 70% 30%,rgba(210,200,190,.8),rgba(210,200,190,0) 70%),
  radial-gradient(ellipse 120px 90px at 40% 60%,rgba(190,60,50,.55),rgba(190,60,50,0) 70%),
  linear-gradient(135deg,#1e1e1e 0%,#4a3a34 45%,#8d7a70 75%,#c9c3bd 100%)}
.photo-mic{background:
  radial-gradient(ellipse 70px 150px at 50% 40%,rgba(20,20,25,.9),rgba(20,20,25,0) 75%),
  radial-gradient(ellipse 180px 120px at 50% 15%,rgba(120,160,255,.7),rgba(120,160,255,0) 70%),
  linear-gradient(180deg,#1b3fbf 0%,#2d62ea 55%,#14307a 80%,#0a1535 100%)}
.photo-room{background:
  radial-gradient(ellipse 200px 90px at 50% 70%,rgba(60,70,85,.9),rgba(60,70,85,0) 75%),
  linear-gradient(180deg,#dfe8f2 0%,#a9bdd6 30%,#4f73a3 55%,#2c4a73 75%,#23262c 100%)}
.round-arrow{position:absolute;top:390px;width:40px;height:40px;border-radius:50%;background:var(--white);border:1px solid var(--line);display:flex;align-items:center;justify-content:center}

/* welcome */
.welcome{position:absolute;top:1449px;left:0;width:1200px;height:622px;background:var(--grey-band)}
.notch{position:absolute;left:580px;width:0;height:0;border-left:20px solid transparent;border-right:20px solid transparent}
.welcome .intro{position:absolute;top:184px;width:100%;text-align:center;font-size:14px;line-height:26px;color:var(--text)}
.feature{position:absolute;white-space:nowrap}
.feature h4{font-size:12px;font-weight:600;color:var(--ink);margin-bottom:6px}
.feature p{font-size:12px;color:var(--muted)}
.feature.left{right:836px;text-align:right}
.feature.right{left:835px;text-align:left}
.f-icon{position:absolute;width:40px;height:40px;border-radius:50%;border:1.5px solid var(--ink);background:var(--white);display:flex;align-items:center;justify-content:center}
.centre-brand{position:absolute;left:525px;top:318px;width:150px;display:flex;flex-direction:column;align-items:center;gap:14px}
.centre-brand .mark{width:150px;height:150px;background:var(--ink)}
.centre-brand span{font-size:20px;font-weight:500;color:var(--ink);white-space:nowrap}

/* pricing */
.pricing{position:absolute;top:2071px;left:0;width:1200px;height:763px;background:var(--black-band);color:var(--white)}
.pricing .heading{color:var(--white)}
.pricing .rule{background:var(--white)}
.plan{position:absolute;top:205px;width:296px;height:471px;border:1px solid var(--price-line)}
.plan h3{height:56px;display:flex;align-items:center;justify-content:center;text-align:center;font-size:16px;font-weight:600;line-height:20px;border-bottom:1px solid var(--price-line)}
.tier{border-bottom:1px solid var(--price-line);text-align:center;display:flex;flex-direction:column;justify-content:center}
.tier:last-child{border-bottom:none}
.tier b{font-size:34px;font-weight:500;display:block;margin-bottom:6px}
.tier span{font-size:11px;line-height:16px;color:#dddddd}
.tier span strong{color:var(--white)}

/* video: hand on mixing console photo area */
.video{position:absolute;top:2834px;left:0;width:1200px;height:498px;background:
  radial-gradient(ellipse 260px 200px at 18% 30%,rgba(200,110,80,.8),rgba(200,110,80,0) 70%),
  radial-gradient(ellipse 300px 160px at 30% 75%,rgba(60,30,25,.85),rgba(60,30,25,0) 70%),
  radial-gradient(ellipse 420px 300px at 78% 55%,rgba(226,206,204,.85),rgba(226,206,204,0) 70%),
  linear-gradient(120deg,#4a2018 0%,#8a4030 30%,#b8857a 55%,#d4bcb8 80%,#9a7a74 100%)}
.play{position:absolute;left:554px;top:190px;width:100px;height:100px;border-radius:50%;border:4px solid var(--white);display:flex;align-items:center;justify-content:center}
.video h2{position:absolute;left:784px;top:240px;font-size:32px;font-weight:400;letter-spacing:2px;color:var(--white)}
.video p{position:absolute;left:784px;top:302px;width:300px;font-size:18px;line-height:32px;color:var(--ink)}
.video .btn{position:absolute;left:787px;top:396px;width:127px;height:41px;background:var(--ink);color:var(--white);font-size:12px;font-weight:600;display:flex;align-items:center;justify-content:center}

/* map + contact */
.map{position:absolute;top:3332px;left:0;width:1200px;height:558px;background:
  radial-gradient(ellipse 300px 140px at 88% 30%,rgba(246,220,150,.55),rgba(246,220,150,0) 70%),
  radial-gradient(ellipse 200px 120px at 6% 85%,rgba(160,200,230,.6),rgba(160,200,230,0) 70%),
  linear-gradient(135deg,#ebe9e4 0%,#dfe1df 50%,#d6dde2 100%)}
.qc-card{position:absolute;left:376px;top:135px;width:425px;height:307px;background:var(--white);box-shadow:0 4px 18px rgba(0,0,0,.18)}
.qc-card h3{position:absolute;left:30px;top:28px;font-size:22px;font-weight:400;letter-spacing:2px;color:var(--ink)}
.qc-card hr{position:absolute;left:0;top:76px;width:100%;border:none;border-top:1px solid var(--line)}
.qc-row{position:absolute;left:40px;display:flex;align-items:center;gap:26px;font-size:16px;letter-spacing:1px;color:var(--ink);line-height:24px;white-space:nowrap}
.qc-row .c-ico{width:34px;height:34px;border-radius:50%;border:1px solid var(--line);display:flex;align-items:center;justify-content:center;flex:none}

/* footer */
.footer{position:absolute;top:3890px;left:0;width:1200px;height:447px}
.footer .brand{top:86px}
.footer .follow{position:absolute;left:192px;top:184px;font-size:12px;font-weight:600;color:var(--ink)}
.soc{position:absolute;top:222px;width:30px;height:30px;border-radius:50%}
.col-title{position:absolute;top:72px;font-size:12px;font-weight:600;color:var(--ink)}
.foot-menu{position:absolute;left:434px;top:104px;list-style:none;font-size:12px;line-height:24px;color:var(--text)}
.field{position:absolute;border:1px solid var(--line);font-size:10px;color:var(--text);padding:10px 12px}
.submit{position:absolute;left:960px;top:262px;width:107px;height:38px;background:var(--ink);color:var(--white);font-size:13px;font-weight:600;display:flex;align-items:center;justify-content:center}
.foot-rule{position:absolute;left:133px;top:360px;width:934px;border-top:1px solid var(--line)}
.copyright{position:absolute;top:406px;width:100%;text-align:center;font-size:11px;color:var(--text)}
</style>
</head>
<body>
<div class="page">

  <header class="topbar">
    <div class="abs follow">Follow us : <span class="dot"></span><span class="dot"></span><span class="dot"></span><span class="dot"></span></div>
    <div class="abs contact">
      <span class="sq-icon"><svg width="12" height="9" viewBox="0 0 12 9"><rect x="0.5" y="0.5" width="11" height="8" fill="none" stroke="#fff"/><path d="M0.5 0.5 6 5 11.5 0.5" fill="none" stroke="#fff"/></svg></span>
      <span>Lvasquezstudio@quillmarkpost.com</span>
      <span style="width:26px"></span>
      <span class="sq-icon"><svg width="11" height="11" viewBox="0 0 24 24"><path d="M6.6 10.8a15 15 0 0 0 6.6 6.6l2.2-2.2c.3-.3.7-.4 1-.2 1.1.4 2.3.6 3.6.6.6 0 1 .4 1 1V20c0 .6-.4 1-1 1A17 17 0 0 1 3 4c0-.6.4-1 1-1h3.5c.6 0 1 .4 1 1 0 1.3.2 2.5.6 3.6.1.3 0 .7-.2 1z" fill="#fff"/></svg></span>
      <span>417-392-7048</span>
    </div>
  </header>

  <nav class="nav">
    <div class="brand"><span class="mark"></span>Dorn Studio 817</div>
    <ul class="menu">
      <li class="active">HOME</li><li>ABOUT US</li><li>STUDIOS</li><li>SERVICES</li><li>MUSIC</li><li>VIDEOS</li><li>BLOG</li><li>CONTACT</li>
    </ul>
  </nav>

  <section class="hero" role="img" aria-label="Photo of a recording studio control room with a large mixing console, wooden desk and studio monitors">
    <div class="slide-arrow" style="left:0"><svg width="12" height="18" viewBox="0 0 12 18"><path d="M10 2 3 9l7 7" fill="none" stroke="#fff" stroke-width="2.5"/></svg></div>
    <div class="slide-arrow" style="right:0"><svg width="12" height="18" viewBox="0 0 12 18"><path d="M2 2l7 7-7 7" fill="none" stroke="#fff" stroke-width="2.5"/></svg></div>
    <h1>MUSIC RECORDING STUDIO</h1>
    <div class="btn">LEARN MORE</div>
  </section>

  <section class="services">
    <h2 class="heading" style="top:78px">OUR SERVICES</h2>
    <div class="rule" style="top:135px"></div>
    <div class="card" style="left:133px"><div class="photo photo-faders" role="img" aria-label="Close-up photo of mixing desk faders and knobs"></div><p>MUSIC RECORDING</p></div>
    <div class="card" style="left:450px"><div class="photo photo-mic" role="img" aria-label="Photo of a studio condenser microphone against blue light"></div><p>COMPOSING ROOM</p></div>
    <div class="card" style="left:767px"><div class="photo photo-room" role="img" aria-label="Photo of a studio recording room with console and monitors"></div><p>STUDIO ROOM</p></div>
    <div class="round-arrow" style="left:110px"><svg width="8" height="12" viewBox="0 0 8 12"><path d="M6 1 1 6l5 5" fill="none" stroke="#111" stroke-width="1.6"/></svg></div>
    <div class="round-arrow" style="left:1048px"><svg width="8" height="12" viewBox="0 0 8 12"><path d="M2 1l5 5-5 5" fill="none" stroke="#111" stroke-width="1.6"/></svg></div>
  </section>

  <section class="welcome">
    <div class="notch" style="top:0;border-top:20px solid var(--white)"></div>
    <h2 class="heading" style="top:70px">WELCOME TO OUR SITE</h2>
    <div class="rule" style="top:132px"></div>
    <p class="intro">There are many variations of passages of Lorem Ipsum available, but the majority have suffered alteration<br>in some form, by injected humour, or randomised words which don't look.</p>

    <svg class="abs" style="left:0;top:0" width="1200" height="622" aria-hidden="true">
      <g fill="none" stroke="#111" stroke-width="1.5">
        <path d="M440 313h70v40"/><path d="M440 405h70"/><path d="M440 517h70v-40"/>
        <path d="M761 313h-71v40"/><path d="M761 405h-71"/><path d="M761 517h-71v-40"/>
      </g>
    </svg>

    <div class="feature left" style="top:296px"><h4>HIGH QUALITY RECORDING</h4><p>There are many variations of passages of</p></div>
    <div class="feature left" style="top:392px"><h4>MUSIC PRODUCTION</h4><p>There are many variations of passages of</p></div>
    <div class="feature left" style="top:506px"><h4>PROFESSIONAL MIXING</h4><p>There are many variations of passages of</p></div>
    <div class="feature right" style="top:296px"><h4>GET SUPPORT</h4><p>There are many variations of passages of</p></div>
    <div class="feature right" style="top:392px"><h4>POST PRODUCTION</h4><p>There are many variations of passages of</p></div>
    <div class="feature right" style="top:506px"><h4>TEAM</h4><p>There are many variations of passages of</p></div>

    <div class="f-icon" style="left:400px;top:293px"><svg width="18" height="18" viewBox="0 0 24 24"><rect x="9" y="2" width="6" height="12" rx="3" fill="#111"/><path d="M5 11a7 7 0 0 0 14 0M12 18v4" fill="none" stroke="#111" stroke-width="2"/></svg></div>
    <div class="f-icon" style="left:400px;top:385px"><svg width="18" height="18" viewBox="0 0 24 24"><path d="M6 3v18M12 3v18M18 3v18" stroke="#111" stroke-width="2"/><rect x="4" y="7" width="4" height="3" fill="#111"/><rect x="10" y="13" width="4" height="3" fill="#111"/><rect x="16" y="9" width="4" height="3" fill="#111"/></svg></div>
    <div class="f-icon" style="left:400px;top:497px"><svg width="18" height="18" viewBox="0 0 24 24"><rect x="2" y="6" width="20" height="12" rx="2" fill="none" stroke="#111" stroke-width="2"/><path d="M6 10h2M10 10h2M14 10h2M6 14h12" stroke="#111" stroke-width="2"/></svg></div>
    <div class="f-icon" style="left:761px;top:293px"><svg width="18" height="18" viewBox="0 0 24 24"><path d="M4 14v-2a8 8 0 0 1 16 0v2" fill="none" stroke="#111" stroke-width="2"/><rect x="3" y="13" width="4" height="7" rx="1" fill="#111"/><rect x="17" y="13" width="4" height="7" rx="1" fill="#111"/></svg></div>
    <div class="f-icon" style="left:761px;top:385px"><svg width="18" height="18" viewBox="0 0 24 24"><rect x="3" y="5" width="18" height="12" rx="1" fill="none" stroke="#111" stroke-width="2"/><path d="M8 21h8M12 17v4" stroke="#111" stroke-width="2"/></svg></div>
    <div class="f-icon" style="left:761px;top:497px"><svg width="18" height="18" viewBox="0 0 24 24"><circle cx="12" cy="8" r="3" fill="#111"/><circle cx="5" cy="10" r="2.2" fill="#111"/><circle cx="19" cy="10" r="2.2" fill="#111"/><path d="M6 20a6 6 0 0 1 12 0M1 19a4 4 0 0 1 5-4M23 19a4 4 0 0 0-5-4" fill="none" stroke="#111" stroke-width="2"/></svg></div>

    <div class="centre-brand"><div class="mark"></div><span>Dorn Studio 817</span></div>
  </section>

  <section class="pricing">
    <div class="notch" style="top:0;border-top:20px solid var(--grey-band)"></div>
    <h2 class="heading" style="top:74px">PRICING</h2>
    <div class="rule" style="top:130px"></div>

    <div class="plan" style="left:133px">
      <h3>RECORDING PRICE</h3>
      <div class="tier" style="height:101px"><b>$80</b><span>per hour minimum <strong>4 hours</strong> required</span></div>
      <div class="tier" style="height:101px"><b>$75</b><span>per hour minimum <strong>8 hours</strong> required</span></div>
      <div class="tier" style="height:101px"><b>$70</b><span>per hour minimum <strong>12 hours</strong> required</span></div>
      <div class="tier" style="height:110px"><b>$90</b><span>for individual hours, packages recommended</span></div>
    </div>
    <div class="plan" style="left:452px">
      <h3>MEMBERSHIPS DEALS</h3>
      <div class="tier" style="height:138px"><b>$1500</b><span>get 48 recording hours in addition<br>to 24 hours mix down</span></div>
      <div class="tier" style="height:138px"><b>$2500</b><span>get 72 recording hours in addition<br>to 48 hours mix down</span></div>
      <div class="tier" style="height:137px"><b>$3500</b><span>get 96 recording hours in addition<br>to 72 hours mix down</span></div>
    </div>
    <div class="plan" style="left:771px">
      <h3>MIX DOWN<br>ONLY PRICES</h3>
      <div class="tier" style="height:101px"><b>$50</b><span>per hour minimum <strong>4 hours</strong> required</span></div>
      <div class="tier" style="height:101px"><b>$45</b><span>per hour minimum <strong>8 hours</strong> required</span></div>
      <div class="tier" style="height:101px"><b>$40</b><span>per hour minimum 12 hours required</span></div>
      <div class="tier" style="height:110px"><b>$60</b><span>for individual hours, packages recommended</span></div>
    </div>
  </section>

  <section class="video" role="img" aria-label="Photo of a hand turning a knob on a mixing console">
    <div class="play"><svg width="34" height="40" viewBox="0 0 34 40"><path d="M4 2 32 20 4 38z" fill="#fff"/></svg></div>
    <h2>VIDEOS</h2>
    <p>It is a long established fact that a reader will be distracted.</p>
    <div class="btn">WATCH VIDEO</div>
  </section>

  <section class="map" role="img" aria-label="Street map showing the studio location in Miramar, Florida">
    <div class="qc-card">
      <h3>QUICK CONTACT</h3>
      <hr>
      <div class="qc-row" style="top:106px"><span class="c-ico"><svg width="12" height="16" viewBox="0 0 12 16"><path d="M6 0a6 6 0 0 0-6 6c0 4.5 6 10 6 10s6-5.5 6-10a6 6 0 0 0-6-6z" fill="#111"/><circle cx="6" cy="6" r="2.2" fill="#fff"/></svg></span><span>6172 BRAMWELL CT,<br>MIRAMAR, FL, 33081</span></div>
      <div class="qc-row" style="top:188px"><span class="c-ico"><svg width="14" height="14" viewBox="0 0 24 24"><path d="M6.6 10.8a15 15 0 0 0 6.6 6.6l2.2-2.2c.3-.3.7-.4 1-.2 1.1.4 2.3.6 3.6.6.6 0 1 .4 1 1V20c0 .6-.4 1-1 1A17 17 0 0 1 3 4c0-.6.4-1 1-1h3.5c.6 0 1 .4 1 1 0 1.3.2 2.5.6 3.6.1.3 0 .7-.2 1z" fill="#111"/></svg></span><span>417-392-7048</span></div>
      <div class="qc-row" style="top:250px"><span class="c-ico"><svg width="14" height="11" viewBox="0 0 14 11"><rect width="14" height="11" fill="#111"/><path d="M0.5 0.5 7 6 13.5 0.5" fill="none" stroke="#fff"/></svg></span><span>Lvasquezstudio@quillmarkpost.com</span></div>
    </div>
  </section>

  <footer class="footer">
    <div class="brand"><span class="mark"></span>Dorn Studio 817</div>
    <div class="follow">FOLLOW US</div>
    <span class="soc" style="left:162px;background:var(--soc-1)" aria-label="Social link"></span>
    <span class="soc" style="left:208px;background:var(--soc-2)" aria-label="Social link"></span>
    <span class="soc" style="left:254px;background:var(--soc-3)" aria-label="Social link"></span>

    <div class="col-title" style="left:434px">MENU</div>
    <ul class="foot-menu"><li>Home</li><li>About us</li><li>Studios</li><li>Services</li><li>Music</li><li>Videos</li><li>Blog</li><li>Contact us</li></ul>

    <div class="col-title" style="left:610px">QUICK CONTACT</div>
    <div class="field" style="left:613px;top:106px;width:220px;height:38px">Name</div>
    <div class="field" style="left:613px;top:154px;width:220px;height:38px">E mail</div>
    <div class="field" style="left:613px;top:202px;width:220px;height:38px">Phone</div>
    <div class="field" style="left:847px;top:106px;width:220px;height:136px">Message</div>
    <div class="submit">SUBMIT</div>

    <div class="foot-rule"></div>
    <div class="copyright">Copyright @ 2017 All Rights Reserved</div>
  </footer>

</div>
</body>
</html>
```